New Office Poster Designs

Attached you will find 3 poster designs that we found online along with our logos. Please use our logos to reference any type of color or design.
These posters will be hung around our Loan Offices.

INSTRUCTIONS: Please mimic all 3 posters (MINUS THE SMALL WRITING ON THEM THAT IS NOT IN ENGLISH IGNORE THAT)
but use our logos and colors. Also, if you can make them in Spanish as well as English that is a plus. We will also need 1 additional poster with the below wording.

Additional Poster:
Stuck in a Title Loan? Let us pay it off up to $10,000

Target Market(s)

People looking to get a loan and need money

Industry/Entity Type

Loan Industry - Consumer Lending - Fast easy loans

Requirements
Nice to have
• English and Spanish

```html
<!DOCTYPE html>
<html lang="en">
<head>
<meta charset="utf-8">
<title>Title Loan Payoff Posters – English &amp; Spanish</title>
<link href="https://fonts.googleapis.com/css2?family=Poppins:wght@300;400;500;600;700;800&display=swap" rel="stylesheet">
<style>
  :root {
    --board: #dcdcdc;
    --label: #1f3a2a;
    --poster-base: #0c5a2f;
    --poster-light: #17703c;
    --band-dark: rgba(2, 38, 16, 0.55);
    --frame: #1ee86a;
    --accent: #27ee6c;
    --white: #ffffff;
    --red: #d0202a;
  }
  * { box-sizing: border-box; margin: 0; padding: 0; }
  html, body { width: 1200px; height: 911px; overflow: hidden; }
  body {
    background: var(--board);
    font-family: "Poppins", sans-serif;
    position: relative;
  }
  .version-label {
    position: absolute;
    top: 60px;
    width: 490px;
    text-align: center;
    font-size: 24px;
    font-weight: 400;
    color: var(--label);
    letter-spacing: 0.5px;
  }
  .poster {
    position: absolute;
    top: 139px;
    width: 490px;
    height: 633px;
    overflow: hidden;
    box-shadow: 0 4px 12px rgba(0,0,0,0.25);
  }
  .poster--en, .version-label--en { left: 69px; }
  .poster--es, .version-label--es { left: 629px; }
  .money-backdrop {
    position: absolute; inset: 0;
    background:
      radial-gradient(ellipse at 30% 20%, var(--poster-light), transparent 60%),
      radial-gradient(ellipse at 80% 80%, #14683a, transparent 55%),
      var(--poster-base);
  }
  .band-dark {
    position: absolute; left: 0; right: 0;
    top: 191px; height: 268px;
    background: var(--band-dark);
  }
  .poster--es .band-dark { top: 205px; height: 254px; }
  .frame {
    position: absolute;
    left: 14px; right: 14px; top: 18px; height: 597px;
    border: 2px solid var(--frame);
  }
  .headline { position: absolute; left: 0; right: 0; text-align: center; font-weight: 700; line-height: 1; }
  .headline--accent { color: var(--accent); }
  .headline--main { color: var(--white); }
  .poster--en .h1 { top: 54px; font-size: 47px; letter-spacing: -0.5px; }
  .poster--en .h2 { top: 99px; font-size: 60px; letter-spacing: -1px; }
  .poster--es .h1 { top: 43px; font-size: 38px; }
  .poster--es .h2 { top: 90px; font-size: 40px; }
  .poster--es .h3 { top: 135px; font-size: 40px; }
  .offer { position: absolute; left: 0; right: 0; text-align: center; font-weight: 700; line-height: 1; }
  .offer-lead { top: 226px; font-size: 28px; color: var(--white); }
  .offer-upto { top: 258px; font-size: 28px; color: var(--accent); }
  .offer-amount { top: 284px; font-size: 74px; color: var(--white); letter-spacing: -1px; }
  .offer-amount sup { font-size: 36px; vertical-align: 26px; margin-right: 2px; }
  .swoosh { position: absolute; left: 170px; top: 365px; }
  .icon-slot {
    position: absolute; left: 215px; top: 385px; width: 60px; height: 52px;
    background: rgba(255,255,255,0.12); border-radius: 6px;
  }
  .contact { position: absolute; left: 40px; top: 480px; }
  .contact-tag { font-size: 20px; font-weight: 300; color: var(--accent); letter-spacing: 1.5px; line-height: 1.2; }
  .contact-phone { display: flex; align-items: center; gap: 5px; font-size: 24px; font-weight: 700; color: var(--white); line-height: 1.2; }
  .contact-web {
    display: inline-block; margin-top: 3px;
    background: var(--red); color: var(--white);
    font-size: 10px; font-weight: 500; padding: 1px 5px; border-radius: 3px;
  }
  .brand {
    position: absolute; left: 318px; top: 500px;
    display: flex; align-items: center; gap: 7px;
    font-size: 24px; font-weight: 600; color: var(--white);
  }
  .brand-dot { width: 12px; height: 12px; border-radius: 50%; background: var(--red); }
  .fine-print {
    position: absolute; left: 40px; right: 40px; top: 562px;
    font-size: 6px; line-height: 1.35; color: var(--white); font-weight: 400;
  }
</style>
</head>
<body>

<div class="version-label version-label--en">ENGLISH</div>
<div class="version-label version-label--es">SPANISH</div>

<section class="poster poster--en" lang="en">
  <div class="money-backdrop" role="img" aria-label="Background photo of scattered dollar bills tinted green"></div>
  <div class="band-dark"></div>
  <div class="frame"></div>
  <h1>
    <span class="headline headline--accent h1">STUCK IN A</span>
    <span class="headline headline--main h2">TITLE LOAN?</span>
  </h1>
  <p class="offer offer-lead">LET US PAY IT OFF</p>
  <p class="offer offer-upto">UP TO</p>
  <p class="offer offer-amount"><sup>$</sup>10,000</p>
  <svg class="swoosh" width="150" height="36" viewBox="0 0 150 36"><path d="M2 34 Q75 -14 148 30 Q75 -2 2 34Z" fill="var(--red)"/></svg>
  <div class="icon-slot" role="img" aria-label="Icon of a car resting on an open hand with a dollar coin"></div>
  <div class="contact">
    <p class="contact-tag">Limited time</p>
    <p class="contact-phone">
      <svg width="12" height="12" viewBox="0 0 24 24"><path d="M6.6 10.8a15 15 0 0 0 6.6 6.6l2.2-2.2a1 1 0 0 1 1-.25 11.4 11.4 0 0 0 3.6.57 1 1 0 0 1 1 1V20a1 1 0 0 1-1 1A17 17 0 0 1 3 4a1 1 0 0 1 1-1h3.5a1 1 0 0 1 1 1c0 1.25.2 2.45.57 3.6a1 1 0 0 1-.25 1z" fill="var(--accent)"/></svg>
      +36 1 555 0199
    </p>
    <span class="contact-web">www.crestpay.com</span>
  </div>
  <div class="brand"><span class="brand-dot"></span>Crestpay</div>
  <p class="fine-print">Applying for a personal installment loan with Crestpay Financial is easy. Texas loan rates | Loan amounts $2,500 – $10,000 | APR range 27.58% – 35.99% | Terms 12 – 24 months | Your terms may vary based on credit history, income, debts and collateral. Borrowing $10,000 at 27.58% APR over 24 months, payments would be $546.74 per month, total cost $13,121.69. Example based on a standard 650–780 credit score.</p>
</section>

<section class="poster poster--es" lang="es">
  <div class="money-backdrop" role="img" aria-label="Foto de fondo de billetes de dólar esparcidos en tono verde"></div>
  <div class="band-dark"></div>
  <div class="frame"></div>
  <h1>
    <span class="headline headline--accent h1">ATRAPADO EN UN</span>
    <span class="headline headline--main h2">¿PRÉSTAMO DE</span>
    <span class="headline headline--main h3">TÍTULO?</span>
  </h1>
  <p class="offer offer-lead">VAMOS A PAGARLO</p>
  <p class="offer offer-upto">HASTA</p>
  <p class="offer offer-amount"><sup>$</sup>10,000</p>
  <svg class="swoosh" width="150" height="36" viewBox="0 0 150 36"><path d="M2 34 Q75 -14 148 30 Q75 -2 2 34Z" fill="var(--red)"/></svg>
  <div class="icon-slot" role="img" aria-label="Icono de un auto sobre una mano abierta con una moneda de dólar"></div>
  <div class="contact">
    <p class="contact-tag">Tiempo limitado</p>
    <p class="contact-phone">
      <svg width="12" height="12" viewBox="0 0 24 24"><path d="M6.6 10.8a15 15 0 0 0 6.6 6.6l2.2-2.2a1 1 0 0 1 1-.25 11.4 11.4 0 0 0 3.6.57 1 1 0 0 1 1 1V20a1 1 0 0 1-1 1A17 17 0 0 1 3 4a1 1 0 0 1 1-1h3.5a1 1 0 0 1 1 1c0 1.25.2 2.45.57 3.6a1 1 0 0 1-.25 1z" fill="var(--accent)"/></svg>
      +36 1 555 0199
    </p>
    <span class="contact-web">www.crestpay.com</span>
  </div>
  <div class="brand"><span class="brand-dot"></span>Crestpay</div>
  <p class="fine-print">Solicitar un préstamo personal a plazos con Crestpay Financial es fácil. Tasas de Texas | Montos de $2,500 – $10,000 | Rango APR 27,58% – 35,99% | Plazos de 12 a 24 meses | Sus términos pueden variar según historial crediticio, ingresos, deudas y garantía. Con $10,000 al 27,58% en 24 meses, pagaría $546.74 al mes, costo total $13,121.69. Ejemplo basado en un puntaje de 650 a 780.</p>
</section>

</body>
</html>
```